Stationery Design Project

I need a design that is simple, clean and modern, in square style, bold font.
The majority of the design needs to be White and Black with a splash of Red colour.
I would like a design for business cards and letter heads with the following information.
Name, Title, Phone, Fax, Email, Website and company ABN number

Target Market(s)

25 to 65 years old real estate clients

Industry/Entity Type

Business

Requirements
Must have
• All designs must incorporate Company Logo, Name, Title, Phone, Fax, Email, Website and company ABN number

```html
<!DOCTYPE html>
<html lang="en">
<head>
<meta charset="utf-8">
<title>Northgate Real Estate – Stationery</title>
<link href="https://fonts.googleapis.com/css2?family=Open+Sans:wght@400;600;700&display=swap" rel="stylesheet">
<style>
  :root {
    --stage: #58585a;
    --black: #151515;
    --black-soft: #2e2e2e;
    --red: #e01b22;
    --paper: #f6f7f7;
    --white: #ffffff;
    --ink: #3a3a3a;
    --mark-faint: rgba(255,255,255,0.05);
    --mark-light: #ebebeb;
  }
  * { box-sizing: border-box; margin: 0; padding: 0; }
  html, body { width: 1200px; height: 1160px; overflow: hidden; }
  body {
    background: var(--stage);
    font-family: "Open Sans", Arial, sans-serif;
    position: relative;
  }
  .dark-band {
    background: linear-gradient(90deg, #0c0c0c 0%, var(--black-soft) 50%, #0c0c0c 100%);
  }
  .brand-name {
    font-family: "Open Sans", Arial, sans-serif;
    font-weight: 700;
    color: var(--white);
    text-transform: uppercase;
    text-align: center;
    line-height: 1.1;
    letter-spacing: 0.04em;
  }
  .label { font-weight: 700; margin-right: 4px; }

  /* Business card – front */
  .card-front {
    position: absolute; left: 23px; top: 55px; width: 184px; height: 320px;
    border-radius: 9px; overflow: hidden;
    background: linear-gradient(90deg, #111 0%, #303030 50%, #111 100%);
  }
  .card-front .edge { position: absolute; left: 0; right: 0; height: 20px; background: var(--red); }
  .card-front .edge.top { top: 0; }
  .card-front .edge.bottom { bottom: 0; }
  .card-front .mark-area {
    position: absolute; left: 10px; top: 30px; width: 150px; height: 270px;
    background: radial-gradient(ellipse at 40% 45%, var(--mark-faint) 0%, transparent 70%);
  }
  .card-front .brand-name {
    position: absolute; left: 15px; top: 132px; width: 155px; font-size: 20px;
  }

  /* Business card – back */
  .card-back {
    position: absolute; left: 218px; top: 55px; width: 185px; height: 320px;
    border-radius: 9px; overflow: hidden; background: var(--paper);
  }
  .card-back .brand-name {
    position: absolute; left: 20px; top: 56px; width: 145px; font-size: 15px; color: var(--black);
  }
  .card-back .person { position: absolute; top: 126px; width: 100%; text-align: center; }
  .card-back .person-name { color: var(--red); font-weight: 700; font-size: 18px; line-height: 1.2; }
  .card-back .person-title { color: var(--black); font-size: 13px; line-height: 1.2; }
  .card-back .contact-panel {
    position: absolute; left: 0; top: 178px; width: 100%; height: 122px;
  }
  .card-back .contact-panel .mark-area {
    position: absolute; left: 0; top: 0; width: 100%; height: 100%;
    background: radial-gradient(ellipse at 30% 40%, var(--mark-faint) 0%, transparent 70%);
  }
  .card-back .phones, .card-back .online, .card-back .abn {
    position: absolute; width: 100%; text-align: center; font-size: 11px;
  }
  .card-back .phones { top: 12px; color: var(--white); line-height: 18px; }
  .card-back .online { top: 58px; color: var(--red); line-height: 15px; }
  .card-back .abn { top: 96px; color: var(--white); line-height: 15px; font-size: 10px; }
  .card-back .red-rule { position: absolute; left: 0; top: 300px; width: 100%; height: 4px; background: var(--red); }

  /* Letterhead */
  .letterhead {
    position: absolute; left: 422px; top: 41px; width: 745px; height: 1054px;
    background: var(--paper); overflow: hidden;
  }
  .letterhead .head-rule { position: absolute; left: 0; top: 24px; width: 100%; height: 4px; background: var(--red); }
  .letterhead .head-band { position: absolute; left: 0; top: 28px; width: 100%; height: 92px; }
  .letterhead .head-band .brand-name {
    position: absolute; left: 0; top: 28px; width: 100%; font-size: 20px;
  }
  .letterhead .mark-area {
    position: absolute; left: 0; top: 410px; width: 380px; height: 563px;
    background: radial-gradient(ellipse at 45% 50%, var(--mark-light) 0%, rgba(235,235,235,0.4) 55%, transparent 75%);
  }
  .letterhead .footer-contacts {
    position: absolute; right: 32px; top: 986px; font-size: 12.5px; color: var(--ink);
    display: flex; gap: 12px; white-space: nowrap;
  }
  .letterhead .footer-contacts .label { color: var(--red); }
  .letterhead .foot-rule { position: absolute; left: 0; top: 1021px; width: 100%; height: 4px; background: var(--red); }
  .letterhead .foot-band { position: absolute; left: 0; top: 1025px; width: 100%; height: 29px; }
</style>
</head>
<body>

  <section class="card-front" aria-label="Business card front">
    <div class="edge top"></div>
    <div class="mark-area" role="img" aria-label="Faint brand symbol decoration"></div>
    <div class="brand-name">Northgate<br>Real Estate</div>
    <div class="edge bottom"></div>
  </section>

  <section class="card-back" aria-label="Business card back">
    <div class="brand-name">Northgate<br>Real Estate</div>
    <div class="person">
      <p class="person-name">Liam Carter</p>
      <p class="person-title">President</p>
    </div>
    <div class="contact-panel dark-band">
      <div class="mark-area" role="img" aria-label="Faint brand symbol decoration"></div>
      <p class="phones"><span class="label">P</span>(555) 014-2290<br><span class="label">F</span>(555) 014-2291</p>
      <p class="online">liam@northgatere.com<br>www.NorthgateRE.com</p>
      <p class="abn">ABN 12 345 678 901</p>
    </div>
    <div class="red-rule"></div>
  </section>

  <section class="letterhead" aria-label="Letterhead">
    <div class="head-rule"></div>
    <header class="head-band dark-band">
      <div class="brand-name">Northgate<br>Real Estate</div>
    </header>
    <div class="mark-area" role="img" aria-label="Large faint brand symbol watermark"></div>
    <footer class="footer-contacts">
      <span><span class="label">P</span>(555) 014-2290</span>
      <span><span class="label">F</span>(555) 014-2291</span>
      <span>liam@northgatere.com</span>
      <span>www.NorthgateRE.com</span>
      <span>ABN 12 345 678 901</span>
    </footer>
    <div class="foot-rule"></div>
    <div class="foot-band dark-band"></div>
  </section>

</body>
</html>
```